Brochure Design Project

Color brochure with text, graphics, and photos. (I will provide the text). 4 pages of 8 1/2 X 11". This is a brochure about dental implants.
Attached is the text and logo for the brochure.

See new parameters and information on the brochure project.

Included in the brochure is our address: Briar Ridge Dental Care, 418 North Cedar Avenue, Briar Ridge, PA 17943.  717-829-4617.  www.briarridgedentalcare.example.

Martin R. Pike, D.M.D., M.A.G.D., F.I.C.O.I. (Attached is photo for brochure)file://localhost/Users/mrpdmd7/Pictures/iPhoto%20Library/Masters/2003/Office%20Pictures/Dr.%20Pike%202.jpg

Target Market(s)

Adults, primarily senior adults.

Industry/Entity Type

Dental

```html
<!DOCTYPE html>
<html lang="en">
<head>
<meta charset="utf-8">
<title>Dental Implants Brochure – Briar Ridge Dental Care</title>
<link rel="stylesheet" href="https://fonts.googleapis.com/css2?family=Source+Sans+3:wght@300;400;600;700&family=Open+Sans:wght@400;700&display=swap">
<style>
:root{
  --ink:#1e1e1e;
  --body:#333;
  --muted:#8c8c8c;
  --green:#8ea52c;
  --green-soft:#a9c24a;
  --blue:#6fa6d6;
  --blue-deep:#3f7fbf;
  --sky:#9cc0e6;
  --panel:#ececec;
  --paper:#fff;
}
*{box-sizing:border-box;margin:0;padding:0}
html,body{width:1200px;height:900px;overflow:hidden;background:var(--paper)}
body{position:relative;font-family:"Open Sans",Arial,sans-serif;color:var(--body)}
.printer-marks{position:absolute;left:0;top:0}
.page-label{position:absolute;font-family:"Source Sans 3",Arial,sans-serif;font-size:22px;color:#111;width:200px;text-align:center}
.page{position:absolute;background:var(--paper)}
.p-back{left:340px;top:60px;width:265px;height:340px}
.p-front{left:605px;top:60px;width:275px;height:340px}
.p-inner-left{left:337px;top:530px;width:268px;height:355px}
.p-inner-right{left:605px;top:530px;width:275px;height:355px}

/* back page */
.portrait{position:absolute;left:20px;top:10px;width:28px;height:52px;background:linear-gradient(180deg,#8a8f96,#3a3f48)}
.dangers-banner{position:absolute;left:48px;top:22px;width:158px;height:13px;background:linear-gradient(90deg,#2f6fb0,var(--blue) 70%,#e2eef8);color:#fff;font:700 5.2px/13px "Open Sans",sans-serif;padding-left:16px;border-radius:0 7px 7px 0}
.dangers-sub{position:absolute;left:65px;top:42px;font:700 7px "Open Sans",sans-serif;color:var(--green)}
.section-head{display:flex;align-items:center;gap:3px;font:400 6.4px/1.2 "Source Sans 3",sans-serif;color:var(--ink);margin:6px 0 5px -8px}
.section-head::before{content:"";width:6px;height:6px;border-radius:50%;background:radial-gradient(circle at 35% 35%,#c8dc6e,var(--green));flex:none}
.back-copy{position:absolute;left:30px;top:66px;width:226px}
.back-copy p{font-size:4.6px;line-height:1.45;color:var(--ink);margin-bottom:4px}
.back-copy .section-head{margin-top:8px}
.back-address{position:absolute;left:0;top:318px;width:265px;text-align:center;font:700 4.6px/1.6 "Open Sans",sans-serif;color:var(--ink)}
.back-address .web{font-size:5.4px}

/* front page */
.hero-can{position:absolute;left:10px;top:6px;font:300 46px/1 "Source Sans 3",sans-serif;color:#a8b83e;letter-spacing:-1px}
.hero-smile{position:absolute;left:82px;top:34px;font:400 15px/1 "Source Sans 3",sans-serif;color:#333}
.hero-break{position:absolute;left:118px;top:51px;font:400 9.5px/1 "Source Sans 3",sans-serif;color:#333}
.hero-you{position:absolute;left:145px;top:56px;font:300 56px/1 "Source Sans 3",sans-serif;color:var(--sky);letter-spacing:-1px}
.hero-photo{position:absolute;left:6px;top:133px;width:269px;height:129px;background:linear-gradient(160deg,#f1e5dc 0%,#dcc9bd 28%,#b7cfe8 45%,#6f9bd0 75%,#9ec1e7 100%)}
.front-tagline{position:absolute;left:82px;top:270px;font:300 13.5px "Source Sans 3",sans-serif;color:var(--muted)}
.practice-mark{position:absolute;right:14px;top:304px;display:flex;align-items:center;gap:4px;font:400 5px "Source Sans 3",sans-serif;color:var(--muted)}
.practice-mark .dot{width:26px;height:26px;border-radius:50%;background:#3d6e8c}

/* inner pages */
.magic-banner{position:absolute;left:0;top:18px;width:140px;height:11px;background:linear-gradient(90deg,#2f6fb0,var(--blue) 70%,#e2eef8);color:#fff;font:700 5px/11px "Open Sans",sans-serif;padding-left:9px;border-radius:0 6px 6px 0}
.col{position:absolute}
.col p{font-size:4.2px;line-height:1.45;color:var(--ink);margin-bottom:3px;text-align:justify}
.col .section-head{font-size:5.4px;margin:5px 0 3px 0}
.il-c1{left:16px;top:38px;width:118px}
.il-c2{left:148px;top:38px;width:116px}
.ir-c1{left:14px;top:4px;width:118px}
.ir-c2{left:140px;top:4px;width:124px}
.insurance-note{background:var(--green-soft);color:#fff;font:700 4.4px/1.45 "Open Sans",sans-serif;padding:5px 6px;border-radius:3px;margin-top:6px}
.did-you-know{position:absolute;left:14px;top:168px;font:700 5.4px "Source Sans 3",sans-serif;color:var(--ink)}
.facts-panel{position:absolute;left:12px;top:178px;width:252px;height:138px;background:var(--panel);padding:4px 8px}
.facts-panel p{font-size:4.1px;line-height:1.45;color:var(--ink);margin-bottom:3px}
.facts-panel .section-head{font-size:5px;margin:3px 0 2px 0}
.facts-panel .section-head.strong{font-weight:700}
.facts-slogan{text-align:center;color:var(--green);font:700 5px "Open Sans",sans-serif;margin:3px 0}
</style>
</head>
<body>

<svg class="printer-marks" width="1200" height="900" viewBox="0 0 1200 900" aria-hidden="true">
  <defs>
    <g id="reg">
      <circle r="4.5" fill="none" stroke="#222" stroke-width="0.8"/>
      <path d="M-7 0H7M0-7V7" stroke="#222" stroke-width="0.6"/>
      <circle r="2" fill="#222"/>
    </g>
    <g id="colorbar">
      <rect y="0" width="5" height="7" fill="#00aeef"/>
      <rect y="7" width="5" height="7" fill="#ec008c"/>
      <rect y="14" width="5" height="7" fill="#fff200"/>
      <rect y="21" width="5" height="7" fill="#2e3192"/>
      <rect y="28" width="5" height="7" fill="#ed1c24"/>
      <rect y="35" width="5" height="7" fill="#00a651"/>
      <rect y="42" width="5" height="7" fill="#555"/>
      <rect y="49" width="5" height="7" fill="#111"/>
    </g>
    <g id="graybar">
      <rect x="0" width="5" height="5" fill="#111"/><rect x="6" width="5" height="5" fill="#333"/>
      <rect x="12" width="5" height="5" fill="#555"/><rect x="18" width="5" height="5" fill="#777"/>
      <rect x="24" width="5" height="5" fill="#999"/><rect x="30" width="5" height="5" fill="#bbb"/>
      <rect x="36" width="5" height="5" fill="#ddd"/><rect x="42" width="5" height="5" fill="#eee"/>
    </g>
  </defs>
  <!-- top sheet -->
  <use href="#reg" x="333" y="52"/><use href="#reg" x="883" y="52"/>
  <use href="#reg" x="333" y="398"/><use href="#reg" x="883" y="398"/>
  <use href="#reg" x="605" y="48"/>
  <use href="#colorbar" x="331" y="208"/><use href="#colorbar" x="880" y="208"/>
  <use href="#graybar" x="580" y="408"/>
  <!-- bottom sheet -->
  <use href="#reg" x="333" y="525"/><use href="#reg" x="883" y="525"/>
  <use href="#reg" x="333" y="885"/><use href="#reg" x="883" y="885"/>
  <use href="#reg" x="605" y="520"/>
  <use href="#colorbar" x="331" y="660"/><use href="#colorbar" x="880" y="660"/>
  <use href="#graybar" x="580" y="884"/>
  <g stroke="#222" stroke-width="0.6">
    <path d="M340 42v10M326 60h10M880 42v10M884 60h10M340 410v-8M326 400h10M880 410v-8M884 400h10"/>
    <path d="M337 515v10M323 530h10M880 515v10M884 530h10M337 895v-8M323 885h10M880 895v-8M884 885h10"/>
  </g>
</svg>

<div class="page-label" style="left:345px;top:0">4th Page</div>
<div class="page-label" style="left:665px;top:0">1st Page</div>
<div class="page-label" style="left:360px;top:478px">2nd Page</div>
<div class="page-label" style="left:660px;top:478px">3rd Page</div>

<!-- 4th page: back cover -->
<section class="page p-back">
  <div class="portrait" role="img" aria-label="Portrait photo of Dr. Martin R. Pike"></div>
  <div class="dangers-banner">3 Dangers of Tooth Loss and Poor Fitting Dentures</div>
  <div class="dangers-sub">That You Must Know About!</div>
  <div class="back-copy">
    <h3 class="section-head">Bone Loss Makes You Look Older Quicker</h3>
    <p>Dental implants assist you in looking and feeling younger, because they prevent bone loss. By preventing bone loss that would normally occur with the loss of teeth, your facial structure remains normal and intact. The chances of wrinkling and aging before your time is less likely to happen.</p>
    <p>In other words, every day that you continue to wear dentures you are experiencing bone loss, which makes you look much older than you have to.</p>
    <h3 class="section-head">Dentures Increase Your Risk of Heart Disease and Oral Cancer</h3>
    <p>While tooth loss may seem like a small problem compared with other health and fitness issues, it is often the first sign of bigger health problems for many people and can put them at higher risk for heart disease and oral cancer.</p>
    <p>When dentures don't fit properly, or are not removed daily, it can lead to bone disease and oral cancer. The National Oral Health Council reports that there will be approximately 30,000 new cases of oral cancer this year alone.</p>
    <p>Heart disease has been linked to gum disease. When dentures do not fit correctly, you have a higher chance of oral problems. You must be aware of these concerns because dentures can cause more problems than just discomfort and a poor smile.</p>
    <h3 class="section-head">Dentures May Reduce Your Life Span</h3>
    <p>It's True! Many people with poor fitting dentures or multiple missing back teeth live up to 10 years less. This is due to poor eating habits and stomach problems. Denture wearers tend to eat more processed foods and experience other health problems related to poor eating habits. People today now have alternatives to dentures, and the best solution is dental implants.</p>
    <p>People who get dental implants can finally eat the healthy foods they have been missing such as apples, fresh vegetables, corn on the cob, and even steak!</p>
  </div>
  <div class="back-address">
    Briar Ridge Dental Care, 418 North Cedar Avenue, Briar Ridge, PA 17943. 717-829-4617<br>
    <span class="web">www.briarridgedentalcare.example</span>
  </div>
</section>

<!-- 1st page: front cover -->
<section class="page p-front">
  <h1>
    <span class="hero-can">Can</span>
    <span class="hero-smile">Your Smile</span>
    <span class="hero-break">Make Or Break</span>
    <span class="hero-you">You!</span>
  </h1>
  <div class="hero-photo" role="img" aria-label="Close-up photo of a bright smile against a blue sky with clouds"></div>
  <p class="front-tagline">The Magic of dental implants</p>
  <div class="practice-mark"><span>Briar Ridge Dental Care</span><span class="dot"></span></div>
</section>

<!-- 2nd page: inside left -->
<section class="page p-inner-left">
  <div class="magic-banner">The Magic of dental implants</div>
  <div class="col il-c1">
    <h3 class="section-head">What are Dental Implants?</h3>
    <p>Dental implants are small titanium posts placed in the jaw to replace the roots of missing teeth. They act like natural roots and give a firm base for crowns, bridges or dentures that look and feel like your own teeth.</p>
    <h3 class="section-head">What are the Benefits of Dental Implants?</h3>
    <p>Here is a short list of just a few of the benefits.</p>
    <p>1. Prevents bone loss and keeps the face from sagging, so you look younger for longer.</p>
    <p>2. Better quality of life, with replacement teeth that look, feel and function like natural teeth.</p>
    <p>3. You can live longer, because you are able to eat healthy foods and chew properly again.</p>
    <p>4. Increases the amount of satisfaction you get out of eating and smiling.</p>
    <p>5. Creates more confidence in social situations with a stable, natural smile.</p>
    <p>6. Allows you to eat and talk without worrying about slipping or clicking dentures.</p>
    <p>7. You will be relieved of the daily cleaning routines and adhesives that dentures need.</p>
    <p>8. Implants are a long lasting solution that can serve you well for many years.</p>
  </div>
  <div class="col il-c2">
    <p>9. Implants protect the healthy teeth next to the gap, since nothing is ground down.</p>
    <p>10. Eliminates denture sores and the discomfort of a loose fitting plate.</p>
    <h3 class="section-head">Am I a Candidate for Dental Implants?</h3>
    <p>Most people who are missing one or more teeth and are in good general health are candidates. A careful exam and a scan help us plan treatment that suits your mouth and your goals.</p>
    <h3 class="section-head">How Long Will it Take to Complete the Treatment?</h3>
    <p>You will notice a difference almost immediately. The full process often takes a few months, giving the implant time to bond with the bone before the final teeth are placed.</p>
    <h3 class="section-head">Will I need to have One Implant Placed for each Tooth that is Missing?</h3>
    <p>No. In most cases a few implants can support a whole bridge or denture, saving time and cost while still giving you a firm bite.</p>
  </div>
</section>

<!-- 3rd page: inside right -->
<section class="page p-inner-right">
  <div class="col ir-c1">
    <h3 class="section-head">How do I know if I'm Fit for Implants?</h3>
    <p>Great question. Your overall health and your desire to improve the quality of life are more important than your age. Many patients in their 70s and 80s enjoy implants.</p>
    <h3 class="section-head">How Long Do Implants Last?</h3>
    <p>Research has shown that implants have been successful for over 30 years. With good home care and regular visits they can last a lifetime.</p>
    <h3 class="section-head">Do You Offer Any Warranties?</h3>
    <p>Yes. Even though dental implants have a very high success rate, we stand behind our work and will gladly explain the terms at your consultation.</p>
  </div>
  <div class="col ir-c2">
    <h3 class="section-head">What is the Cost of Implant Treatment?</h3>
    <p>Most people ask this first. The cost depends on the number of implants, the type of teeth chosen and any extra procedures. We will give you a clear written estimate.</p>
    <h3 class="section-head">Does Insurance Cover Dental Implant Treatment?</h3>
    <p>Insurance coverage depends on your individual policy. Most plans cover some part of the treatment.</p>
    <p class="insurance-note">Although many companies exclude implants as a covered benefit, many of them will pay the same benefit they would cover for the lowest cost alternative treatment option (partials and dentures) and some for the diagnostic records.</p>
  </div>
  <h3 class="did-you-know">Did you know...</h3>
  <div class="facts-panel">
    <h4 class="section-head strong">Your quality of your smile has a more direct effect on your life than any other part of your appearance!</h4>
    <p>In fact, most people in one survey say they always remember someone with an especially attractive smile. A healthy smile can help you feel at ease with others, at work and at home, and a poor one can hold you back more than you may realize.</p>
    <p class="facts-slogan">Your Smile Can Make Or Break You!</p>
    <p>For hundreds of years, the way people look has played a part in how they are treated. Today a bright, healthy smile is one of the simplest ways to make a strong first impression.</p>
    <p>So, if a smile is so important, why do so many people hide theirs? Often it is because they are unhappy with missing or loose teeth.</p>
    <h4 class="section-head strong">Are You A Denture Sufferer?</h4>
    <p>Many people live with loose dentures that slip when they talk or eat, and they avoid the foods they love. Implants can hold dentures firmly in place so you can smile again.</p>
    <p>That's the bad news. The good news is every single one of these problems can be corrected at Briar Ridge Dental Care. Read on to find out how!</p>
  </div>
</section>

</body>
</html>
```